Uprising SaaS company needs an attractive business card design

We're an uprising SaaS company who's attempting to attack the rigid car (insurance) claims management market in Europe.
We want to our mighty base order management system, listen to our clients to connect the smart ideas to build something even mightier.
We primarily focus on helping our customers manage their customers' claims/orders and get them resolved as smoothly as possible.
We'd like the business card design to express technical innovation and the fact that we connect smart ideas, as our company slogan indicates.
Contact Information for Business Card
Name, position, website, email, mobile, business address
Font styles to use
Colors
Designer to choose colors to be used in the design.
Look and feel
Each slider illustrates characteristics of the customer's brand and the style your logo design should communicate.

```html
<!DOCTYPE html>
<html lang="en">
<head>
<meta charset="utf-8">
<title>Nexorel Business Card</title>
<link rel="stylesheet" href="https://fonts.googleapis.com/css2?family=Poppins:wght@300;400;500;600;700&display=swap">
<style>
  :root {
    --page: #e9eef3;
    --brand-blue: #1d86cc;
    --brand-blue-light: rgba(255, 255, 255, 0.07);
    --white: #ffffff;
    --tint: #eef6fc;
    --teal: #2aa3b8;
    --gray: #6f6f6f;
    --ink: #2b2b2b;
  }
  * { margin: 0; padding: 0; box-sizing: border-box; }
  html, body { width: 1200px; height: 1200px; overflow: hidden; }
  body {
    background: var(--page);
    font-family: "Poppins", sans-serif;
    position: relative;
  }
  .card {
    position: absolute;
    left: 160px;
    width: 880px;
    height: 503px;
    overflow: hidden;
    border-radius: 4px;
    box-shadow: 0 10px 30px rgba(40, 60, 80, 0.18);
  }
  .card-front { top: 60px; background: var(--brand-blue); }
  .card-back { top: 637px; background: var(--white); }
  .card-shapes { position: absolute; inset: 0; width: 100%; height: 100%; }

  .front-wordmark {
    position: absolute;
    left: 0; right: 0;
    top: 130px;
    text-align: center;
    color: var(--white);
    font-weight: 300;
    font-size: 112px;
    letter-spacing: 2px;
    line-height: 1;
  }
  .front-slogan {
    position: absolute;
    left: 0; right: 0;
    top: 282px;
    text-align: center;
    color: var(--white);
    font-weight: 600;
    font-size: 24px;
    letter-spacing: 0.5px;
  }

  .back-wordmark {
    position: absolute;
    right: 80px;
    top: 62px;
    color: var(--gray);
    font-weight: 300;
    font-size: 80px;
    letter-spacing: 2px;
    line-height: 1;
  }
  .company-name {
    position: absolute;
    right: 80px;
    top: 232px;
    color: var(--gray);
    font-weight: 600;
    font-size: 26px;
  }
  .company-address {
    position: absolute;
    right: 80px;
    top: 292px;
    text-align: right;
    color: var(--ink);
    font-size: 19px;
    line-height: 1.45;
    font-style: normal;
  }
  .person {
    position: absolute;
    left: 64px;
    top: 268px;
  }
  .person-name {
    color: var(--teal);
    font-weight: 700;
    font-size: 40px;
    line-height: 1.1;
  }
  .person-role {
    color: var(--ink);
    font-weight: 600;
    font-size: 18px;
    margin-top: 4px;
  }
  .contact-list { list-style: none; margin-top: 14px; }
  .contact-item {
    display: flex;
    align-items: center;
    gap: 16px;
    color: var(--ink);
    font-size: 20px;
    line-height: 1.7;
  }
  .contact-icon { width: 18px; height: 18px; fill: var(--ink); flex: none; }
</style>
</head>
<body>

<section class="card card-front" aria-label="Card front">
  <svg class="card-shapes" viewBox="0 0 880 503" aria-hidden="true">
    <path d="M0 230 L120 170 Q160 150 200 170 L470 260 Q520 280 480 330 L380 470 Q350 503 300 503 L0 503 Z" fill="var(--brand-blue-light)"/>
    <path d="M160 0 L560 0 L420 230 Q400 260 360 250 L150 190 Q110 180 120 140 Z" fill="var(--brand-blue-light)"/>
    <line x1="40" y1="299" x2="276" y2="299" stroke="#ffffff" stroke-width="2"/>
    <line x1="604" y1="299" x2="840" y2="299" stroke="#ffffff" stroke-width="2"/>
  </svg>
  <div class="front-wordmark">nexorel</div>
  <div class="front-slogan">Bridging Clever Ideas</div>
</section>

<section class="card card-back" aria-label="Card back">
  <svg class="card-shapes" viewBox="0 0 880 503" aria-hidden="true">
    <path d="M0 150 L620 70 Q680 62 720 100 L800 170 Q830 200 810 240 L780 330 Q760 380 810 400 L880 420 L880 503 L0 503 Z" fill="var(--tint)"/>
    <path d="M0 360 L0 503 L480 503 Q530 490 520 440 L500 380 Q485 340 440 340 Z" fill="#ffffff" opacity="0.6"/>
    <rect x="350" y="300" width="90" height="8" fill="var(--teal)"/>
    <line x1="440" y1="280" x2="800" y2="280" stroke="var(--teal)" stroke-width="1.5"/>
    <line x1="440" y1="280" x2="440" y2="308" stroke="var(--teal)" stroke-width="1.5"/>
  </svg>
  <div class="back-wordmark">nexorel</div>
  <div class="company-name">Nexorel GmbH</div>
  <address class="company-address">
    Lindenweg 18b<br>10115 Berlin, Germany
  </address>
  <div class="person">
    <div class="person-name">Jonas Weber</div>
    <div class="person-role">Court Registration</div>
    <ul class="contact-list">
      <li class="contact-item">
        <svg class="contact-icon" viewBox="0 0 24 24" aria-hidden="true"><path d="M6.6 10.8a15.1 15.1 0 0 0 6.6 6.6l2.2-2.2a1 1 0 0 1 1-.25 11.4 11.4 0 0 0 3.6.57 1 1 0 0 1 1 1V20a1 1 0 0 1-1 1A17 17 0 0 1 3 4a1 1 0 0 1 1-1h3.5a1 1 0 0 1 1 1c0 1.250.2 2.450.57 3.570a1 1 0 0 1-.25 1z"/></svg>
        <span>+49 170 5550142</span>
      </li>
      <li class="contact-item">
        <svg class="contact-icon" viewBox="0 0 24 24" aria-hidden="true"><path d="M2 5h20v2l-10 6L2 7z"/><path d="M2 9l10 6 10-6v10H2z"/></svg>
        <span>info@nexorel.com</span>
      </li>
    </ul>
  </div>
</section>

</body>
</html>
```